南谷 睦月というペンネームで活動しているものです。

本業は組織・人財開発領域に特化した支援を行う会社において、
企画の提案、プロジェクトマネジメント、依頼後の進捗管理など、
お客様の中に自身も入りながら、経営を変えていくような支援を行っています。

ご依頼をさせていただく表紙デザインですが、
9月16日にPagoraにて、下記の内容を発行いたしました。
============================
現場を変える人が大切にする4つの視点:
~挑戦した人々の物語から静かに学び取る~

www.bookvale-store.jp/item/Q72KD4MX3N
こちらの内容について、発行に向けた表紙手配が間に合わなかったこともあり、
一旦はデザインを自身で考え、発行をいたしましたが、
表紙は書籍の顔ということもあり、作成依頼を進めることに決めました。

デザイン制作にあたって検討いただきたいのは下記2点です。

検討に当たってのポイントは下記2点です。
① 悩みに対しての答えが見つかるような印象を持てる
② あまり複雑すぎないデザインであること

① 悩みに対しての答えが見つかるような印象を持てる
・取り上げたPagoraでは、スキル・ノウハウ本ではなく、
実践されている方が直面されたエピソードをもとにして、
悩みを解決するためのヒントを取り上げています。
そのようなニュアンスが感じられるようなデザインに期待です。

② あまり複雑なデザインではないこと
・凝ったデザインよりは、わかりやすいデザインを好む方です。
複雑なカラーよりは、色を限りながらも、与えられた題材に対しての
表現を頂けるようなデザインが好みではあります。
※ が、良いものが出てくれば、それ限りではございませんので、
あくまで、現時点の好みとしてお伝えを致します

最終的に今回のコンペでは「R_hoshidaさん」のデザインを採用させて頂きます。
重視した点は改めて、下記の2点がベースとなります。
① 悩みに対しての答えが見つかるような印象を持てる
② あまり複雑なデザインではないこと
絵で①のイメージを喚起しつつ、今回の書籍で押し出していることを文字で強調いただく構成となっており、②の点からも適切と考えて採択をさせて頂きました。

改めて、この度はご提案をいただきましてありがとうございます。

引き続き、個人的な目標としては3か月~6か月に1回の頻度で、
Pagora向けの発行物を執筆していく予定です。
また、このような形でご支援の相談をさせていただきますので、
よろしければ是非、お力添えをどうぞお願い申し上げます。

```html
<!DOCTYPE html>
<html lang="ja">
<head>
<meta charset="utf-8">
<title>現場を変える人が大切にする4つの視点</title>
<link rel="stylesheet" href="https://fonts.googleapis.com/css2?family=Montserrat:wght@700&family=Noto+Sans+JP:wght@500;700;900&display=swap">
<style>
  :root {
    --cover-blue: #2d82c6;
    --ghost-blue: #4f99d6;
    --ink-navy: #17233f;
    --accent-yellow: #f6d83b;
    --cream: #f5ead0;
    --white: #ffffff;
  }
  html, body { margin: 0; padding: 0; overflow: hidden; background: var(--cover-blue); }
  .cover {
    position: relative;
    width: 750px; height: 1200px;
    background: var(--cover-blue);
    overflow: hidden;
    font-family: "Noto Sans JP", sans-serif;
    color: var(--white);
  }
  .series-word {
    position: absolute; left: 20px; top: -28px;
    margin: 0;
    font-family: "Montserrat", sans-serif; font-weight: 700;
    font-size: 118px; letter-spacing: 2px; white-space: nowrap;
    color: var(--ghost-blue);
  }
  .title-column {
    position: absolute; top: 112px; margin: 0;
    writing-mode: vertical-rl;
    font-weight: 900; color: var(--ink-navy);
    line-height: 1; letter-spacing: 2px;
  }
  .title-lead { right: 28px; font-size: 56px; }
  .title-mid-a { right: 118px; font-size: 64px; }
  .title-mid-b { right: 200px; font-size: 64px; }
  .title-key {
    position: absolute; left: 70px; top: 100px;
    margin: 0; width: 200px; text-align: center;
    font-weight: 900; color: var(--accent-yellow); line-height: 0.9;
  }
  .title-key .num { display: block; font-size: 180px; line-height: 0.82; }
  .title-key .kana { display: block; font-size: 92px; line-height: 1; }
  .title-key .kanji { display: block; font-size: 176px; }
  .hero-art {
    position: absolute; left: 262px; top: 300px;
    width: 420px; height: 370px;
  }
  .author { position: absolute; left: 72px; top: 752px; }
  .author-name { margin: 0; font-size: 44px; font-weight: 700; letter-spacing: 6px; }
  .author-roman { margin: 4px 0 0; font-size: 17px; font-weight: 500; letter-spacing: 1px; }
  .subtitle {
    position: absolute; left: 40px; right: 40px; top: 930px;
    margin: 0; font-size: 36px; font-weight: 700; line-height: 1.35;
  }
  .points {
    position: absolute; left: 40px; right: 30px; top: 1055px;
    margin: 0; padding: 0; list-style: none;
    display: flex; flex-wrap: wrap; column-gap: 30px; row-gap: 10px;
    font-size: 22px; font-weight: 500;
  }
  .points li { display: flex; align-items: center; white-space: nowrap; }
  .points li::before {
    content: ""; width: 16px; height: 16px; margin-right: 6px;
    border: 2px solid var(--white); box-sizing: border-box;
  }
</style>
</head>
<body>
<main class="cover">
  <p class="series-word">Four Views</p>

  <h1 class="title">
    <span class="title-column title-lead">現場を変える人が</span>
    <span class="title-column title-mid-a">大切に</span>
    <span class="title-column title-mid-b">する</span>
    <span class="title-key">
      <span class="num">4</span>
      <span class="kana">つの</span>
      <span class="kanji">視点</span>
    </span>
  </h1>

  <svg class="hero-art" viewBox="0 0 420 370" role="img" aria-label="上昇する矢印を抱えて階段を登るビジネスパーソンのイラスト">
    <defs>
      <linearGradient id="artFill" x1="0" y1="0" x2="0" y2="1">
        <stop offset="0" stop-color="#f5ead0"/>
        <stop offset="1" stop-color="#f1d27a"/>
      </linearGradient>
    </defs>
    <path d="M120 20 C230 -10 360 30 400 130 C430 220 380 330 250 355 C130 375 20 320 10 220 C0 120 40 40 120 20 Z" fill="url(#artFill)"/>
  </svg>

  <div class="author">
    <p class="author-name">南谷 睦月</p>
    <p class="author-roman">Minamiya Mutsuki</p>
  </div>

  <p class="subtitle">挑戦した人々の物語から<br>静かに学び取る</p>

  <ul class="points">
    <li>結果を言語化する</li>
    <li>仮の結論を用意する</li>
    <li>適切な働きかけを模索する</li>
    <li>伝えるべきことを整理する</li>
    <li>権力を持たれる方に助力を仰ぐ</li>
  </ul>
</main>
</body>
</html>
```